Real Estate investment company needs billboard designs

This is our website: https://velmarkpropertygroup.com/
We are looking for some billboard concepts that uses our CEO in the design. I have attached some images and 1 billboard design that someone in our industry uses, but we don't want it exactly like his.

Industry/Entity Type

real estate

Colors

Designer to choose colors to be used in the design.

Requirements
Must have
• Company colors from websiute

```html
<!DOCTYPE html>
<html lang="en">
<head>
<meta charset="utf-8">
<title>Velmark Property Group – Billboard</title>
<link rel="stylesheet" href="https://fonts.googleapis.com/css2?family=Poppins:wght@500;700;800&display=swap">
<style>
  :root {
    --navy: #1f1d43;
    --red: #e8222b;
    --white: #ffffff;
    --page: #d9dce1;
    --board-light: #f4f5f7;
    --board-mid: #e4e6e9;
    --board-dark: #cfd2d6;
    --photo-dark: #1c1c22;
    --photo-mid: #3a3a42;
    --photo-skin: #c99a82;
  }
  * { margin: 0; padding: 0; box-sizing: border-box; }
  html, body {
    width: 1200px;
    height: 1178px;
    overflow: hidden;
    background: var(--page);
    font-family: "Poppins", sans-serif;
  }
  .billboard {
    position: absolute;
    left: 0;
    top: 439px;
    width: 1200px;
    height: 300px;
    background: radial-gradient(ellipse at 55% 40%, var(--board-light) 0%, var(--board-mid) 60%, var(--board-dark) 100%);
    overflow: hidden;
  }
  .ceo-photo {
    position: absolute;
    left: 22px;
    top: 108px;
    width: 380px;
    height: 192px;
    background: linear-gradient(180deg, var(--photo-skin) 0%, var(--photo-mid) 30%, var(--photo-dark) 100%);
    border-radius: 6px 6px 0 0;
  }
  .billboard-art {
    position: absolute;
    inset: 0;
    width: 1200px;
    height: 300px;
  }
  .brand-name, .headline, .tagline { font-family: "Poppins", sans-serif; }
  .brand-name { font-weight: 700; fill: var(--navy); }
  .headline { font-weight: 800; }
  .headline-navy { fill: var(--navy); }
  .headline-red { fill: var(--red); }
  .tagline { font-weight: 700; fill: var(--white); }
  .website { font-family: "Poppins", sans-serif; font-weight: 500; fill: var(--red); }
  .rule { stroke: var(--navy); stroke-width: 1.5; }
  .tag-box { fill: var(--red); }
</style>
</head>
<body>
  <section class="billboard" aria-label="Velmark Property Group billboard">
    <div class="ceo-photo" role="img" aria-label="Photo of the company CEO smiling with arms spread wide, wearing a black shirt"></div>
    <svg class="billboard-art" viewBox="0 0 1200 300" xmlns="http://www.w3.org/2000/svg">
      <text class="brand-name" x="96" y="78" font-size="56" textLength="232" lengthAdjust="spacingAndGlyphs">VELMARK</text>
      <text class="brand-name" x="328" y="100" font-size="15" text-anchor="end">PROPERTY GROUP</text>

      <line class="rule" x1="432" y1="22" x2="432" y2="280"/>

      <text class="headline headline-navy" x="464" y="111" font-size="86" textLength="700" lengthAdjust="spacingAndGlyphs">WE BUY HOUSES</text>
      <text class="headline headline-navy" x="464" y="173" font-size="86" textLength="161" lengthAdjust="spacingAndGlyphs">FOR</text>
      <text class="headline headline-red" x="649" y="173" font-size="86" textLength="236" lengthAdjust="spacingAndGlyphs">CASH</text>

      <rect class="tag-box" x="896" y="129" width="270" height="43"/>
      <text class="tagline" x="904" y="159" font-size="22" textLength="254" lengthAdjust="spacingAndGlyphs">FAST. RELIABLE. LOCAL.</text>

      <line class="rule" x1="464" y1="207" x2="1166" y2="207"/>

      <text class="website" x="464" y="260" font-size="56" textLength="702" lengthAdjust="spacingAndGlyphs">velmarkpropertygroup.com</text>
    </svg>
  </section>
</body>
</html>
```